Corporate Design für Tafelrunde bei Sonja
Zielgruppe
Private Dinner
Zielgruppe: Privatpersonen, ab ca 40 Jahre, die gern Kulinarik einmal anders erleben wollen und Gesellschaft und Kommunikation schätzen, da das Konzept vorsieht, dass alle Gäste an einer großen Tafel sitzen, im Vordergrund, steht dabei das gemütliche Anbiete - man fühlt sich wie bei guten Freunden zu Gast
Aufgabenstellung
Eine gewisse Eleganz und Stil ...dem Namen entsprechend
Eine Idee war als Symbol Besteck zu nehmen (Messer und Gabel oder Messer, Gabel, Löffel - etwas verunglückt in der ersten Eigenkompositionsiehe Anhänge zu sehen - das Fleischermesser ist ein einfach furchtbar)
weitere Idee war jetzt als Zeichen/Logo einen symbolischen Tisch/Tafel (mit Gästen?) einfließen zu lassen - da der grobe Unterschied zu anderen Anbietern oder auch Restaurants ist, dass alle Gäste gemeinsam an einem großen Tisch sitzen
Ansonsten sind bisherige Überlegungen und zu transportierende Infos am besten auf den ersten "selbstgestrickten" Foldern zu erlesen
Bei einem zukünftigen Folder würde ich den großen Teil der Menüfolge und den Preis dazu sehr klein halten und nicht so zentral wie jetzt
Am besten gefällt mir daran die Farbe ... eine Mischung aus burgunderrot und braun (die im Druck dann nicht so gut rauskam) - die Farbe hat etwas Edles, das mir zum Namen und Konzept dazu gut gefällt
Ebenso ist das Konzept und die Idee auf www.beisonja.live ausführlich dargestellt

```html
<!DOCTYPE html>
<html lang="de">
<head>
<meta charset="utf-8">
<title>Tafelrunde bei Sonja – Geschäftsausstattung</title>
<link rel="stylesheet" href="https://fonts.googleapis.com/css2?family=Oswald:wght@400;500&family=Open+Sans:wght@400;700&family=Great+Vibes&display=swap">
<style>
  :root {
    --burgundy: #9b1b35;
    --burgundy-deep: #5a0a1d;
    --gold: #c2a46c;
    --ink: #2e2e2e;
    --paper: #ffffff;
    --stage: #3b3b3b;
  }
  * { margin: 0; padding: 0; box-sizing: border-box; }
  html, body { width: 1200px; height: 856px; overflow: hidden; background: var(--stage); }
  .canvas { position: relative; width: 1200px; height: 856px; }

  .letterhead {
    position: absolute; left: 189px; top: 134px; width: 416px; height: 588px;
    background: var(--paper); font-family: "Open Sans", sans-serif; color: var(--ink);
  }
  .wordmark { font-family: "Oswald", sans-serif; font-weight: 400; color: var(--burgundy); letter-spacing: .02em; white-space: nowrap; }
  .letterhead .wordmark { position: absolute; right: 36px; top: 56px; font-size: 13px; }
  .sender-line {
    position: absolute; left: 45px; top: 91px; font-size: 3.6px; font-weight: 700;
    border-bottom: .5px solid var(--ink); padding-bottom: 1px; width: 103px;
  }
  .recipient { position: absolute; left: 45px; top: 106px; font-size: 6.4px; line-height: 8.4px; }
  .recipient .city { margin-top: 8px; }
  .subject { position: absolute; left: 45px; top: 200px; font-size: 6.2px; font-weight: 700; }
  .body-copy { position: absolute; left: 45px; top: 223px; width: 228px; font-size: 5.7px; line-height: 7.6px; }
  .body-copy p + p { margin-top: 7.6px; }
  .closing { position: absolute; left: 45px; top: 419px; font-size: 5.7px; }
  .signature { position: absolute; left: 45px; top: 430px; font-family: "Great Vibes", cursive; font-size: 16px; color: #111; }
  .footer-rule { position: absolute; left: 70px; width: 275px; top: 542px; height: 1.5px; background: var(--burgundy); }
  .footer { position: absolute; left: 70px; width: 275px; top: 551px; display: flex; justify-content: space-between; }
  .footer-col { font-family: "Oswald", sans-serif; font-size: 3.8px; line-height: 5.2px; color: var(--gold); text-align: center; text-transform: uppercase; letter-spacing: .03em; }

  .card { position: absolute; left: 759px; width: 252px; height: 163px; }
  .card--front { top: 215px; background: var(--paper); }
  .card--back { top: 476px; background: var(--burgundy-deep); display: flex; align-items: center; justify-content: center; }
  .card--front .wordmark { position: absolute; left: 0; right: 0; top: 42px; text-align: center; font-size: 17px; }
  .card--back .wordmark { color: var(--gold); font-size: 18px; }
  .card-rule { position: absolute; left: 52px; width: 148px; top: 97px; height: 1px; background: var(--ink); }
  .card-contact {
    position: absolute; left: 0; right: 0; top: 106px; text-align: center;
    font-family: "Oswald", sans-serif; font-size: 7px; line-height: 10.5px; color: var(--burgundy); letter-spacing: .02em;
  }
  .card-contact .web { color: var(--gold); }
  .icon { width: 6px; height: 6px; vertical-align: -0.5px; margin-right: 2px; }
</style>
</head>
<body>
<main class="canvas">

  <article class="letterhead">
    <div class="wordmark">Tafelrunde bei Sonja</div>
    <div class="sender-line">Vorname Nachname, Musterstr. 123, 12345 Musterstadt</div>
    <div class="recipient">
      <div>Martina Musterfrau</div>
      <div>Musterstraße 456</div>
      <div class="city">12345 Berlin</div>
    </div>
    <div class="subject">Quidero molore, atatur sae. Nequat,</div>
    <div class="body-copy">
      <p>Ur sit, imus, ipicatem voluptate eum re dolluptios sequosam, eum reritati am volor sapedissi quo blaboribust, sequass itasped igendi cus exerfer feruptas iusanda ndaest, qui omnis nus aut fugitinis quatur ad ullaut mostem quasperiae corem et aciatem illatin ciduntores quidis utemquam autemperae soluptiae lab illacescia solorum et fugiam ratatatus exerro blaciis samusam etur? Uga. Neque nam simi, nest, ommod essedios magnatia nossi aute nonsequam fugiaspis moluptas sed el int etur saepe nonsecatem excea noneceperrum ulligendit faccullores et lantur si ium at.Ota cuptae non ea de opta voles rem rae dolore ilia vellab isi blanis idit veribus auda alit labore desenis imenis que in con rehent, explat ped que volorum, autent, si tetur?</p>
      <p>Ihil ium restior ecepero reptistius es aborepe diatiunt dignis diciae voluptu ribearit, que nat aute et as maximus, qui blab iur aut volest, nonsequae odios doluptatiae velignimin perescia vent.<br>Pa voluptas expero corectur molest eaquid enda vidus verciis quodi te dit aliquid unturem poreper feratur? Quis aut rehenihilit et quam, eris et perorru mquamusa quo et untia volupie nisimoluptae esseribus cora doluptati doluptatur atisciumqui re pa quat aut lam solescia intiis et millabor sit odis et quos re sam, vendicientur abo. Equi totatus rest, nosam quodi omni doloriosam des ea nimpelique volo elendae dellign ihilitis solupta temporp orupta iuntia ipiste natibusapis volesedis reriori taerrup tatiberes nobitiur, sequi omnihillab id maximagnat omnimus dolo quunt, int aut earum lacit peliquunt iduciet, id que autemolum deruptati te non re.</p>
    </div>
    <div class="closing">Sincerely</div>
    <div class="signature">S. Brendel</div>
    <div class="footer-rule"></div>
    <footer class="footer">
      <div class="footer-col">Vorname Nachname<br>Musterstr. 123<br>12345 Musterstadt</div>
      <div class="footer-col">Tel. 010 · 123 456 789<br>Fax 010 · 123 456 790<br>info@tafelseite.de</div>
      <div class="footer-col">Beispielbank AG<br>IBAN: DE12345677890<br>BIC: MUS940DS90</div>
    </footer>
  </article>

  <section class="card card--front">
    <div class="wordmark">Tafelrunde bei Sonja</div>
    <div class="card-rule"></div>
    <div class="card-contact">
      <div>MUSTERSTR. 123 · 12345 MUSTERSTADT</div>
      <div>
        <svg class="icon" viewBox="0 0 10 10" aria-hidden="true"><path fill="#c2a46c" d="M2 1l2 2-1 1.5c.6 1.2 1.3 1.9 2.5 2.5L7 6l2 2-1.5 1.5C4 9 1 6 .5 2.5z"/></svg>010 / 123 456 78
        &nbsp;&nbsp;
        <svg class="icon" viewBox="0 0 10 10" aria-hidden="true"><path fill="#c2a46c" d="M2 1l2 2-1 1.5c.6 1.2 1.3 1.9 2.5 2.5L7 6l2 2-1.5 1.5C4 9 1 6 .5 2.5z"/></svg>FAX: 010 / 123 456 80
      </div>
      <div>
        <svg class="icon" viewBox="0 0 10 10" aria-hidden="true"><rect x="1" y="2.5" width="8" height="5.5" fill="none" stroke="#c2a46c" stroke-width="1"/><path d="M1 2.5l4 3 4-3" fill="none" stroke="#c2a46c" stroke-width="1"/></svg>INFO@BEISPIELNETZ.DE
      </div>
      <div class="web">WWW.BEISPIELNETZ.DE</div>
    </div>
  </section>

  <section class="card card--back">
    <div class="wordmark">Tafelrunde bei Sonja</div>
  </section>

</main>
</body>
</html>
```